Under Still Skies Stationary Design Pkg
Business Card, Letterhead, #10 Envelope, 4 X 6 Notecard
Under Still Skies Stationary Design Pkg -
Creative Brief
Simple
Marla Quint
Coach/Writer/Speaker
2847 W. Fallow Lane Suite 310 Phoenix, Arizona 85093
marla@understillskies.example
www.understillskies.example
Contest is for a business card, standard letterhead, #10 envelope, and a 4 1/4 X 6 1/4 note card design. Please use the light and dark gray colors from the design. No big solids. On the note card design, please only use the my name (Marla Quint) and logo w/o company name or tag lines. Thank you. I look forward to seeing what you come up with.

```html
<!DOCTYPE html>
<html lang="en">
<head>
<meta charset="utf-8">
<title>Under Still Skies Stationery Package</title>
<link href="https://fonts.googleapis.com/css2?family=Lato:wght@400;700&display=swap" rel="stylesheet">
<style>
  :root {
    --backdrop: #ece9e4;
    --paper: #ffffff;
    --light-gray: #d9d9d9;
    --mid-gray: #a6a6a6;
    --dark-gray: #7b7b7b;
    --ink: #5f5f5f;
    --leaf-tint: #eeeeee;
  }
  * { box-sizing: border-box; margin: 0; padding: 0; }
  html, body { width: 1200px; height: 404px; overflow: hidden; }
  body {
    background: var(--backdrop);
    font-family: "Lato", Arial, sans-serif;
    color: var(--ink);
    position: relative;
  }
  .sheet {
    position: absolute;
    background: var(--paper);
    box-shadow: 0 2px 5px rgba(0,0,0,.18);
    overflow: hidden;
  }
  .leaf-motif {
    position: absolute;
    border-radius: 50%;
    background: radial-gradient(circle, var(--leaf-tint) 0%, rgba(238,238,238,0) 70%);
  }
  .wave {
    position: absolute; left: 0; bottom: 0; width: 100%;
  }
  .brand {
    position: absolute;
    display: flex; align-items: center; gap: 4px;
    font-weight: 700; color: var(--dark-gray);
    letter-spacing: .08em; text-transform: uppercase; white-space: nowrap;
  }
  .brand .dot { border-radius: 50%; background: var(--mid-gray); flex: none; }
  .small-text { position: absolute; line-height: 1.35; color: var(--ink); white-space: nowrap; }
  .signature { position: absolute; font-size: 6px; color: var(--dark-gray); }

  /* note card */
  .note-card { left: 19px; top: 29px; width: 150px; height: 158px; }
  /* business cards */
  .card-front { left: 182px; top: 43px; width: 118px; height: 72px; }
  .card-back { left: 307px; top: 43px; width: 120px; height: 72px; background: var(--mid-gray); }
  .card-back .brand { color: var(--paper); }
  .card-back .brand .dot { background: var(--paper); }
  /* small cards row */
  .note-small { left: 29px; top: 202px; width: 144px; height: 158px; }
  .note-wide { left: 192px; top: 197px; width: 173px; height: 163px; }
  .note-tall { left: 384px; top: 163px; width: 180px; height: 217px; }
  /* letterhead */
  .letterhead { left: 595px; top: 24px; width: 178px; height: 356px; }
  /* envelopes */
  .envelope-back { left: 883px; top: 108px; width: 293px; height: 156px; }
  .envelope-front { left: 780px; top: 211px; width: 295px; height: 149px; }
</style>
</head>
<body>

<!-- Note card, front -->
<div class="sheet note-card">
  <div class="leaf-motif" role="img" aria-label="Faint leaf motif" style="left:-30px;top:-10px;width:150px;height:150px"></div>
  <div class="brand" style="left:92px;top:108px;font-size:5px"><span class="dot" style="width:6px;height:6px"></span>Under Still Skies</div>
  <div class="signature" style="left:104px;top:120px">Marla Quint</div>
  <svg class="wave" viewBox="0 0 150 30" height="30" preserveAspectRatio="none">
    <path d="M0 22 C40 8 90 26 150 10 L150 30 L0 30 Z" fill="var(--mid-gray)"/>
    <path d="M0 18 C45 4 95 22 150 6" stroke="var(--light-gray)" stroke-width="1.5" fill="none"/>
  </svg>
</div>

<!-- Business card, front -->
<div class="sheet card-front">
  <div class="leaf-motif" role="img" aria-label="Faint leaf motif" style="left:-20px;top:-15px;width:90px;height:90px"></div>
  <div class="brand" style="left:36px;top:14px;font-size:6px"><span class="dot" style="width:7px;height:7px"></span>Under Still Skies</div>
  <div class="small-text" style="left:70px;top:34px;font-size:3.5px">
    <strong>Marla Quint</strong><br>Coach/Writer/Speaker<br>2847 W. Fallow Lane Suite 310<br>Phoenix, Arizona 85093<br>marla@understillskies.example<br>www.understillskies.example
  </div>
  <svg class="wave" viewBox="0 0 118 12" height="12" preserveAspectRatio="none">
    <path d="M0 8 C35 0 80 12 118 3 L118 12 L0 12 Z" fill="var(--mid-gray)"/>
  </svg>
</div>

<!-- Business card, back -->
<div class="sheet card-back">
  <div class="brand" style="left:30px;top:14px;font-size:6px"><span class="dot" style="width:7px;height:7px"></span>Under Still Skies</div>
  <div class="small-text" style="left:72px;top:34px;font-size:3.5px;color:var(--paper)">
    <strong>Marla Quint</strong><br>Coach/Writer/Speaker<br>2847 W. Fallow Lane Suite 310<br>Phoenix, Arizona 85093<br>marla@understillskies.example
  </div>
  <svg class="wave" viewBox="0 0 120 12" height="12" preserveAspectRatio="none">
    <path d="M0 8 C35 0 80 12 120 3 L120 12 L0 12 Z" fill="var(--light-gray)"/>
  </svg>
</div>

<!-- Note card, inside -->
<div class="sheet note-small">
  <div class="leaf-motif" role="img" aria-label="Faint leaf motif" style="left:-35px;top:0;width:140px;height:140px"></div>
  <svg class="wave" viewBox="0 0 144 30" height="30" preserveAspectRatio="none">
    <path d="M0 20 C40 6 90 26 144 10 L144 30 L0 30 Z" fill="var(--light-gray)"/>
  </svg>
</div>

<!-- Note card, wide -->
<div class="sheet note-wide">
  <div class="brand" style="left:10px;top:12px;font-size:6px"><span class="dot" style="width:7px;height:7px"></span>Under Still Skies</div>
  <div class="leaf-motif" role="img" aria-label="Faint leaf motif" style="left:90px;top:30px;width:100px;height:100px"></div>
  <svg class="wave" viewBox="0 0 173 30" height="30" preserveAspectRatio="none">
    <path d="M0 20 C50 6 110 26 173 10 L173 30 L0 30 Z" fill="var(--mid-gray)"/>
    <path d="M0 16 C55 2 115 22 173 6" stroke="var(--light-gray)" stroke-width="1.5" fill="none"/>
  </svg>
</div>

<!-- Note card, tall -->
<div class="sheet note-tall">
  <div class="brand" style="left:12px;top:12px;font-size:6px"><span class="dot" style="width:7px;height:7px"></span>Under Still Skies</div>
  <div class="leaf-motif" role="img" aria-label="Faint leaf motif" style="left:80px;top:50px;width:120px;height:120px"></div>
  <svg class="wave" viewBox="0 0 180 34" height="34" preserveAspectRatio="none">
    <path d="M0 22 C55 6 115 30 180 10 L180 34 L0 34 Z" fill="var(--mid-gray)"/>
    <path d="M0 18 C60 2 120 26 180 6" stroke="var(--light-gray)" stroke-width="1.5" fill="none"/>
  </svg>
</div>

<!-- Letterhead -->
<div class="sheet letterhead">
  <div class="brand" style="left:10px;top:12px;font-size:7px"><span class="dot" style="width:8px;height:8px"></span>Under Still Skies</div>
  <div class="small-text" style="left:118px;top:10px;font-size:3.5px">
    2847 W. Fallow Lane Suite 310<br>Phoenix, Arizona 85093<br>marla@understillskies.example<br>www.understillskies.example
  </div>
  <div class="leaf-motif" role="img" aria-label="Faint leaf motif" style="left:60px;top:120px;width:150px;height:150px"></div>
  <svg class="wave" viewBox="0 0 178 40" height="40" preserveAspectRatio="none">
    <path d="M0 26 C55 8 115 34 178 12 L178 40 L0 40 Z" fill="var(--mid-gray)"/>
    <path d="M0 21 C60 3 120 29 178 7" stroke="var(--light-gray)" stroke-width="1.5" fill="none"/>
  </svg>
</div>

<!-- #10 envelope, back -->
<div class="sheet envelope-back">
  <svg style="position:absolute;left:0;top:0" width="293" height="156" viewBox="0 0 293 156">
    <path d="M0 0 L293 0 L293 20 L146 78 L0 20 Z" fill="var(--mid-gray)"/>
    <path d="M0 20 L146 78 L293 20" stroke="var(--light-gray)" stroke-width="1" fill="none"/>
    <path d="M0 156 L146 78 L293 156" stroke="var(--light-gray)" stroke-width=".8" fill="none"/>
  </svg>
  <div class="leaf-motif" role="img" aria-label="Faint leaf motif on flap" style="left:200px;top:-10px;width:80px;height:80px;background:radial-gradient(circle,#c4c4c4 0%,rgba(196,196,196,0) 70%)"></div>
</div>

<!-- #10 envelope, front -->
<div class="sheet envelope-front">
  <div class="brand" style="left:10px;top:10px;font-size:7px"><span class="dot" style="width:8px;height:8px"></span>Under Still Skies</div>
  <div class="small-text" style="left:12px;top:110px;font-size:3.5px">
    2847 W. Fallow Lane Suite 310<br>Phoenix, Arizona 85093
  </div>
  <div class="leaf-motif" role="img" aria-label="Faint leaf motif" style="left:170px;top:0;width:110px;height:110px"></div>
  <svg class="wave" viewBox="0 0 295 24" height="24" preserveAspectRatio="none">
    <path d="M0 16 C90 2 190 22 295 6 L295 24 L0 24 Z" fill="var(--mid-gray)"/>
    <path d="M0 12 C95 -2 195 18 295 2" stroke="var(--light-gray)" stroke-width="1.5" fill="none"/>
  </svg>
</div>

</body>
</html>
```